Brightvantage.com tech company website

Current site is www.brightvantage.com. The site will tell you about our company.

Designs we like are:
http://megainfo.quellorix.com
www.trelvo.com
www.morvasket.com

Target Market(s)

B2B

Industry/Entity Type

It Company

Coding

Coded - Design and coding required

Number of Pages Required

5+ page

Requirements
Must have
• We want to entice without giving away too much info. We like graphics and colors. But website must look official and credible.

```html
<!DOCTYPE html>
<html lang="en">
<head>
<meta charset="utf-8">
<title>Brightvantage.com – Big Data and Analytics</title>
<link href="https://fonts.googleapis.com/css2?family=Open+Sans:wght@400;600;700&display=swap" rel="stylesheet">
<style>
  :root {
    --white: #ffffff;
    --nav-text: #4a4f57;
    --nav-active: #2f8fd0;
    --brand: #2b4a66;
    --heading: #3d4249;
    --body: #8a8f96;
    --line: #d6d8db;
    --space-deep: #0d1630;
    --space-mid: #2a3c70;
    --space-soft: #c8d2e8;
    --footer-bg: #3a4a5c;
    --footer-text: #c5ced8;
    --photo-sand: #d9c7ad;
    --photo-grey: #9aa3aa;
    --photo-amber: #9a6330;
    --photo-cream: #e6d8c6;
    --photo-blush: #e2cbb8;
    --photo-slate: #8c96a0;
    --photo-bronze: #7a5230;
    --photo-wheat: #cdb58e;
  }
  * { margin: 0; padding: 0; box-sizing: border-box; }
  html, body { width: 747px; height: 1200px; overflow: hidden; }
  body {
    font-family: "Open Sans", Arial, sans-serif;
    background: var(--white);
    position: relative;
  }

  .site-header {
    position: absolute; top: 0; left: 0; width: 747px; height: 32px;
    background: var(--white);
    display: flex; align-items: center;
    padding-left: 135px;
    z-index: 3;
  }
  .brand { display: flex; align-items: center; gap: 5px; color: var(--brand);
    font-weight: 700; font-size: 9px; letter-spacing: .8px; white-space: nowrap; }
  .brand-dot { width: 10px; height: 10px; border-radius: 50%; background: var(--brand); }
  .main-nav { display: flex; gap: 10px; margin-left: 38px; }
  .main-nav a { font-size: 6px; font-weight: 600; color: var(--nav-text);
    text-decoration: none; letter-spacing: .3px; white-space: nowrap; }
  .main-nav a.is-active { color: var(--nav-active); }

  .space-backdrop {
    position: absolute; top: 32px; left: 0; width: 747px; height: 1098px;
    background: linear-gradient(to bottom,
      var(--space-deep) 0px,
      var(--space-mid) 110px,
      var(--space-soft) 190px,
      #ffffff 300px,
      #ffffff 730px,
      var(--space-soft) 780px,
      var(--space-mid) 840px,
      var(--space-deep) 1098px);
    z-index: 0;
  }

  .page-title {
    position: absolute; top: 85px; left: 0; width: 747px; text-align: center;
    color: var(--white); font-size: 13px; font-weight: 700; letter-spacing: 1px;
    z-index: 2;
  }

  .timeline { position: absolute; left: 0; top: 0; width: 747px; height: 1130px; z-index: 2; }
  .timeline-line { position: absolute; left: 374px; top: 220px; width: 1px; height: 762px;
    background: var(--line); }

  .milestone { position: absolute; left: 0; width: 747px; height: 66px; }
  .milestone-photo {
    position: absolute; left: 342px; top: 0; width: 65px; height: 65px; border-radius: 50%;
    border: 3px solid var(--white); box-shadow: 0 1px 4px rgba(0,0,0,.18);
  }
  .milestone-text { position: absolute; top: 2px; width: 180px; }
  .milestone--left .milestone-text { left: 148px; text-align: right; }
  .milestone--right .milestone-text { left: 424px; text-align: left; }
  .milestone-title { font-size: 7.5px; font-weight: 700; color: var(--heading);
    letter-spacing: .4px; line-height: 1.35; margin-bottom: 4px; }
  .milestone-copy { font-size: 6.5px; line-height: 1.55; color: var(--body); }
  .milestone--on-dark .milestone-title { color: var(--white); }
  .milestone--on-dark .milestone-copy { color: #c9d0de; }

  .site-footer {
    position: absolute; top: 1130px; left: 0; width: 747px; height: 70px;
    background: var(--footer-bg); padding: 22px 0 0 200px; z-index: 3;
  }
  .site-footer .brand { color: var(--white); font-size: 9px; }
  .site-footer .brand-dot { background: var(--white); }
  .copyright { margin-top: 5px; font-size: 5.5px; color: var(--footer-text); letter-spacing: .4px; }
</style>
</head>
<body>
  <header class="site-header">
    <div class="brand"><span class="brand-dot"></span>BRIGHTVANTAGE</div>
    <nav class="main-nav">
      <a href="#">HOME</a>
      <a href="#">ABOUT</a>
      <a href="#" class="is-active">BIG DATA AND ANALYTICS</a>
      <a href="#">PROMOTIONS AND INFLUENCE</a>
      <a href="#">CASE STUDIES</a>
      <a href="#">CONTACT</a>
    </nav>
  </header>

  <div class="space-backdrop" role="img" aria-label="Starry galaxy photograph behind the page, fading to white in the middle"></div>

  <h1 class="page-title">BIG DATA AND ANALYTICS</h1>

  <main class="timeline">
    <div class="timeline-line"></div>

    <section class="milestone milestone--left" style="top:188px">
      <div class="milestone-text">
        <h2 class="milestone-title">UNIQUE INSIGHTS<br>BY BIG DATA EXPERTS</h2>
        <p class="milestone-copy">Our analysts turn vast streams of raw data into clear, actionable insight, helping leaders see patterns early and act with confidence across every market they serve.</p>
      </div>
      <div class="milestone-photo" role="img" aria-label="Photo for unique insights" style="background:var(--photo-sand)"></div>
    </section>

    <section class="milestone milestone--right" style="top:290px">
      <div class="milestone-photo" role="img" aria-label="Photo for targeted marketing" style="background:var(--photo-grey)"></div>
      <div class="milestone-text">
        <h2 class="milestone-title">TRULY TARGETED MARKETING</h2>
        <p class="milestone-copy">Reach the right audience at the right moment. We combine behavioural signals and audience data to shape campaigns that speak directly to the buyers who matter most.</p>
      </div>
    </section>

    <section class="milestone milestone--left" style="top:393px">
      <div class="milestone-text">
        <h2 class="milestone-title">LEAD GENERATION</h2>
        <p class="milestone-copy">We identify qualified prospects through smart data models, filling your pipeline with leads that are ready to talk and likely to convert.</p>
      </div>
      <div class="milestone-photo" role="img" aria-label="Photo for lead generation" style="background:var(--photo-amber)"></div>
    </section>

    <section class="milestone milestone--right" style="top:505px">
      <div class="milestone-photo" role="img" aria-label="Photo for data management" style="background:var(--photo-cream)"></div>
      <div class="milestone-text">
        <h2 class="milestone-title">DATA MANAGEMENT</h2>
        <p class="milestone-copy">We structure, clean and secure your information so teams can find what they need quickly, with one trusted source of truth across the business.</p>
      </div>
    </section>

    <section class="milestone milestone--left" style="top:623px">
      <div class="milestone-text">
        <h2 class="milestone-title">DATA MONETIZATION</h2>
        <p class="milestone-copy">Unlock new revenue from the data you already own. We help you package, value and share information assets in ways that create lasting returns.</p>
      </div>
      <div class="milestone-photo" role="img" aria-label="Photo for data monetization" style="background:var(--photo-blush)"></div>
    </section>

    <section class="milestone milestone--right" style="top:730px">
      <div class="milestone-photo" role="img" aria-label="Photo for influencer targeting" style="background:var(--photo-slate)"></div>
      <div class="milestone-text">
        <h2 class="milestone-title">INFLUENCER IDENTIFICATION<br>AND TARGETING</h2>
        <p class="milestone-copy">Find the voices that shape opinion in your field. We map networks of influence and help you engage the people your customers trust.</p>
      </div>
    </section>

    <section class="milestone milestone--left milestone--on-dark" style="top:838px">
      <div class="milestone-text">
        <h2 class="milestone-title">BUSINESS INTELLIGENCE</h2>
        <p class="milestone-copy">Clear dashboards and reports give every decision maker a live view of performance, so strategy rests on facts rather than guesswork.</p>
      </div>
      <div class="milestone-photo" role="img" aria-label="Photo for business intelligence" style="background:var(--photo-bronze)"></div>
    </section>

    <section class="milestone milestone--right milestone--on-dark" style="top:950px">
      <div class="milestone-photo" role="img" aria-label="Photo for competitive advantage" style="background:var(--photo-wheat)"></div>
      <div class="milestone-text">
        <h2 class="milestone-title">COMPETITIVE ADVANTAGE</h2>
        <p class="milestone-copy">Stay one step ahead. Our insight into markets, rivals and customer trends shows where to move next and how to stay in front.</p>
      </div>
    </section>
  </main>

  <footer class="site-footer">
    <div class="brand"><span class="brand-dot"></span>BRIGHTVANTAGE</div>
    <p class="copyright">COPYRIGHT BRIGHTVANTAGE LLC 2014</p>
  </footer>
</body>
</html>
```